Trance Guide Coaching Marketing Materials
Brochure, Postcard, Business Card, Letterhead, Envelope
I've been in non-stop meetings all week, and I apologize for not being quicker with feedback. I'll comment again this evening. Thank you.
I find myself tied up today on other business. I extended the project a couple of days. This will be the only extension. I will choose a winner promptly when the contest closes, as I did with my previous projects. There may be some final tweaking but everything will be completed within a week of closing, no longer than that. I appreciate all your wonderful creative efforts. Thank you, and may you prosper and thrive happily. Kindest regards.
#22 and #8 good but the people shown have no context. The people depicted should be going about their positive activity or business and not necessarily looking directly into the camera.
#23 interesting design but the people are too frenetic, too much energy. Thank you.
Lots of quality work here, everyone. Thank you. Keep on keepin' on. I will review more this evening (EST) and will extend the contest a day or two at least. The entries are very good. I have to be away from my desk the rest of the day, but I will return here later.
#19 try replacing the guy with outstretched arms. He's cool but we should see more ideas in that spot. Play with it.
I'll talk about other designs later today, as indicated in my earlier note. thanks again.
I have a lot to review today. Thank you for your excellent efforts. I may not comment further until this evening, but please keep on keepin' on.
I am considering extending the contest a few days to give everyone time to react to the comments I make later.
Good work, everyone. Thank you.
I meant #6 quite excellent in below comment today (not #4, which was discussed earlier). Sorry for any confusion. Thank you for the effort.
I may have to extend this contest.
#7 I like this, too. Very good, but needs more variety of people. Tricky but that's why you're the designer! Thank you for the effort.
#4 quite excellent. I'm liking it, but it needs something, not sure what. I see 3 out 5 people white, including both women white. Try mixing it up if you can, although I see from a design point of view the poses and angles work. It could be close.
#3 I gave it 3 stars because the designs are good except for the groups of people, which I already talked about. I want to encourage you, though.
Draft #4, the picture of the guy is interesting. I have to sleep on that one.
Draft #3 and #4: About pictures: I'm not looking for groups of people, and I'm not looking for abstract settings. Pictures should feature individuals in typical settings. Examples: business man, business woman, musician, athlete, teacher, sales person. No couples, no groups. Individuals with whom people reading the brochure can identify.
Thank you.
Thank you for your entries. I'll be reviewing entries tomorrow and offering suggestions.
Designers: Logo AI has been uploaded. Please refer to the Creative Brief and proceed. - Dave
Trance Guide Coaching Contact Info
Gordon P Whitfield CLC CCH
4629 Larkmoor Rd Ste 310
Albany NY 12203
phone 518-926-3081
fax 888-547-2263
web http://TranceGuideNow.example

```html
<!DOCTYPE html>
<html lang="en">
<head>
<meta charset="utf-8">
<title>Trance Guide Coaching – Stationery Set</title>
<link href="https://fonts.googleapis.com/css2?family=Montserrat:wght@700&family=Open+Sans:wght@400;600;700;800&display=swap" rel="stylesheet">
<style>
:root{
  --bg:#e6e6e8;
  --paper:#ffffff;
  --navy:#17215e;
  --blue:#2b3d9c;
  --green:#7cbc2a;
  --ink:#2b2b2b;
  --muted:#8a8f9c;
  --faint:#eceef3;
}
*{box-sizing:border-box;margin:0;padding:0}
html,body{width:1200px;height:967px;overflow:hidden;background:var(--bg)}
body{font-family:"Open Sans",Arial,sans-serif;color:var(--ink)}
.canvas{position:relative;width:1200px;height:967px;overflow:hidden;background:var(--bg)}
.piece{position:absolute;background:var(--paper);box-shadow:0 3px 10px rgba(0,0,0,.18);overflow:hidden}
.swoosh{position:absolute;left:0;width:100%;display:block}
.brand{font-family:"Montserrat",Arial,sans-serif;font-weight:700;color:var(--navy);display:flex;align-items:center;gap:5px;line-height:1;white-space:nowrap}
.brand::before{content:"";width:.9em;height:.9em;border-radius:50%;background:var(--green);flex:none}
.brand--light{color:#fff}
.brand-line{font-family:"Montserrat",Arial,sans-serif;font-weight:700;color:var(--navy);line-height:1;white-space:nowrap}
.photo{position:absolute}
.photo--dark{background:linear-gradient(135deg,#3a3a3e,#7b7b80 60%,#c9c9cc)}
.photo--park{background:linear-gradient(180deg,#9cc77a,#5f9b47 55%,#3f6d31)}
.photo--office{background:linear-gradient(135deg,#c6ccd6,#8f9aac 60%,#e8e8ea)}
.photo--sky{background:linear-gradient(180deg,#7fb3e5,#c9def2 70%,#f2f2f2)}
.photo--portrait{background:linear-gradient(135deg,#d8cfc6,#a89582 60%,#f1ebe4)}
.photo--class{background:linear-gradient(135deg,#48524c,#7b857e 55%,#d9d4cb)}
.headline{font-family:"Open Sans",Arial,sans-serif;font-weight:800;font-style:italic;color:var(--navy);line-height:1.05;text-align:right;white-space:nowrap}
.headline--light{color:#fff}
.panel{position:absolute;top:0;bottom:0;overflow:hidden}
.panel + .panel{border-left:1px solid rgba(0,0,0,.06)}
.h3{font-weight:700;color:#fff;font-size:9px;margin-bottom:4px}
.copy{font-size:6.5px;line-height:1.45;color:#dfe3f5}
.copy--dark{color:#555}
.contact{font-size:7px;line-height:1.5;color:#fff}
.contact--dark{color:var(--navy)}
.blue-fill{background:linear-gradient(180deg,var(--blue),var(--navy))}
.fax-title{font-weight:700;font-size:22px;color:var(--ink);letter-spacing:.5px}
.fax-grid{display:grid;grid-template-columns:1fr 1fr;column-gap:16px;row-gap:8px;font-size:8px;color:#555}
.fax-grid span{display:block;border-bottom:1px solid #bbb;padding-bottom:2px}
.checks{display:flex;gap:10px;font-size:6.5px;color:#555}
.checks span{display:flex;align-items:center;gap:3px}
.checks span::before{content:"";width:7px;height:7px;border:1px solid #888}
.footer-contact{position:absolute;right:14px;text-align:right;font-size:6px;line-height:1.5;color:#fff}
.faint-mark{position:absolute;border-radius:50%;background:var(--faint)}
.card{position:absolute;box-shadow:0 2px 6px rgba(0,0,0,.2);overflow:hidden}
.card--blue{background:linear-gradient(180deg,var(--blue),var(--navy))}
.card--white{background:#fff}
.card--green{background:linear-gradient(135deg,#8fcf3a,#5f9e1c)}
.stamp{position:absolute;border:1px solid #bbb;width:34px;height:40px}
.addr-lines span{display:block;border-bottom:1px solid #ccc;height:12px}
</style>
</head>
<body>
<svg width="0" height="0" style="position:absolute" aria-hidden="true">
  <defs>
    <symbol id="swoosh" viewBox="0 0 100 40" preserveAspectRatio="none">
      <path d="M0,4 Q50,30 100,4 L100,40 L0,40Z" fill="#7cbc2a"/>
      <path d="M0,9 Q50,36 100,9 L100,40 L0,40Z" fill="#2b3d9c"/>
      <path d="M0,20 Q50,40 100,20 L100,40 L0,40Z" fill="#17215e" opacity=".6"/>
    </symbol>
    <symbol id="swoosh-up" viewBox="0 0 100 40" preserveAspectRatio="none">
      <path d="M0,30 Q60,-4 100,14 L100,40 L0,40Z" fill="#7cbc2a"/>
      <path d="M0,35 Q60,2 100,19 L100,40 L0,40Z" fill="#2b3d9c"/>
    </symbol>
  </defs>
</svg>

<main class="canvas">

  <!-- Brochure outside -->
  <section class="piece brochure-outside" style="left:58px;top:26px;width:296px;height:326px;background:var(--navy)">
    <div class="panel" style="left:0;width:99px;background:linear-gradient(180deg,var(--blue),var(--navy));padding:12px 8px">
      <div class="h3">Our Approach</div>
      <p class="copy">Gentle sessions help you find focus, calm and lasting confidence.</p>
      <div class="photo photo--portrait" role="img" aria-label="Photo of a smiling woman" style="left:0;right:0;top:210px;height:116px"></div>
    </div>
    <div class="panel" style="left:99px;width:98px;background:#fff">
      <div class="photo photo--dark" role="img" aria-label="Photo of a violinist playing" style="left:0;right:0;top:0;height:130px"></div>
      <div class="headline" style="position:absolute;right:6px;top:82px;font-size:10px;color:#fff">Bringing Out<br>the Best in<br>You</div>
      <div class="photo photo--sky" role="img" aria-label="Photo of a businessman with open arms on a rooftop" style="left:10px;right:10px;top:135px;height:60px"></div>
      <svg class="swoosh" style="top:200px;height:126px" aria-hidden="true"><use href="#swoosh-up" width="100%" height="100%"/></svg>
    </div>
    <div class="panel" style="left:197px;width:99px;background:#fff">
      <div class="brand" style="position:absolute;left:8px;top:14px;font-size:9px">Trance Guide</div>
      <div class="brand-line" style="position:absolute;left:21px;top:27px;font-size:9px">Coaching</div>
      <svg class="swoosh" style="top:150px;height:176px" aria-hidden="true"><use href="#swoosh" width="100%" height="100%"/></svg>
      <div class="contact" style="position:absolute;left:8px;bottom:28px">
        <div>(518) 926-3081</div><div>(888) 547-2263</div>
      </div>
      <div class="contact" style="position:absolute;left:8px;bottom:10px;font-size:5.5px">http://TranceGuideNow.example</div>
    </div>
  </section>

  <!-- Brochure inside -->
  <section class="piece brochure-inside" style="left:365px;top:26px;width:418px;height:326px;background:var(--navy)">
    <div class="panel blue-fill" style="left:0;width:139px;padding:12px 10px">
      <div class="h3">What We Offer</div>
      <p class="copy">Personal coaching that unlocks the strengths you already carry within.</p>
      <div class="photo photo--dark" role="img" aria-label="Photo of a musician practising" style="left:10px;right:10px;top:80px;height:90px"></div>
      <div class="photo photo--office" role="img" aria-label="Photo of a businessman working at a laptop" style="left:0;right:0;top:230px;height:96px"></div>
    </div>
    <div class="panel" style="left:139px;width:140px;background:var(--navy)">
      <div class="photo photo--park" role="img" aria-label="Photo of a runner on a park path" style="left:0;right:0;top:0;height:215px"></div>
      <svg class="swoosh" style="top:150px;height:176px" aria-hidden="true"><use href="#swoosh" width="100%" height="100%"/></svg>
      <div class="headline headline--light" style="position:absolute;right:10px;top:226px;font-size:10px">Bringing Out the Best in</div>
      <div class="headline headline--light" style="position:absolute;right:10px;top:239px;font-size:20px">You</div>
      <div class="brand brand--light" style="position:absolute;left:10px;top:278px;font-size:7.5px">Trance Guide Coaching</div>
      <div class="contact" style="position:absolute;left:10px;top:292px">(518) 926-3081</div>
    </div>
    <div class="panel blue-fill" style="left:279px;width:139px;padding:12px 10px">
      <div class="h3">How It Works</div>
      <p class="copy">Each session builds clarity, motivation and steady progress toward goals.</p>
      <div class="photo photo--class" role="img" aria-label="Photo of a teacher standing by a chalkboard" style="left:0;right:0;top:200px;height:126px"></div>
    </div>
  </section>

  <!-- Postcard front -->
  <section class="piece postcard-front" style="left:808px;top:210px;width:340px;height:142px">
    <div class="photo photo--dark" role="img" aria-label="Photo of a violinist playing" style="left:0;top:0;width:100%;height:142px"></div>
    <div class="headline" style="position:absolute;left:18px;top:12px;font-size:13px;color:var(--green);text-align:left">Bringing Out<br>the Best in You</div>
    <svg class="swoosh" style="top:90px;height:52px" aria-hidden="true"><use href="#swoosh" width="100%" height="100%"/></svg>
    <div class="brand" style="position:absolute;left:14px;top:80px;font-size:9px">Trance Guide Coaching</div>
    <div class="contact" style="position:absolute;right:14px;bottom:6px;font-size:6px">(518) 926-3081 · http://TranceGuideNow.example</div>
  </section>

  <!-- Postcard back -->
  <section class="piece postcard-back" style="left:808px;top:376px;width:340px;height:146px">
    <div style="position:absolute;left:14px;top:12px;width:150px">
      <div class="h3" style="color:var(--navy)">Book a Session</div>
      <p class="copy copy--dark">Call today to begin your journey.</p>
    </div>
    <div style="position:absolute;left:172px;top:10px;bottom:40px;border-left:1px solid #ccc"></div>
    <div class="stamp" style="right:14px;top:10px"></div>
    <div class="addr-lines" style="position:absolute;left:184px;right:20px;top:56px"><span></span><span></span><span></span></div>
    <div class="brand" style="position:absolute;left:14px;top:90px;font-size:8px">Trance Guide Coaching</div>
    <svg class="swoosh" style="top:108px;height:38px" aria-hidden="true"><use href="#swoosh" width="100%" height="100%"/></svg>
  </section>

  <!-- Letterhead -->
  <section class="piece letterhead" style="left:78px;top:425px;width:262px;height:358px">
    <div class="brand" style="position:absolute;left:18px;top:18px;font-size:9px">Trance Guide Coaching</div>
    <div class="faint-mark" role="img" aria-label="Faint brand circle" style="left:88px;top:110px;width:86px;height:86px"></div>
    <svg class="swoosh" style="top:268px;height:90px" aria-hidden="true"><use href="#swoosh" width="100%" height="100%"/></svg>
    <div class="footer-contact" style="bottom:10px">
      Gordon P Whitfield CLC CCH<br>4629 Larkmoor Rd Ste 310, Albany NY 12203<br>518-926-3081 · 888-547-2263<br>http://TranceGuideNow.example
    </div>
  </section>

  <!-- Fax cover -->
  <section class="piece fax" style="left:378px;top:425px;width:314px;height:358px">
    <div class="brand" style="position:absolute;left:18px;top:18px;font-size:9px">Trance Guide Coaching</div>
    <div class="fax-title" style="position:absolute;left:18px;top:70px">FAX</div>
    <div class="fax-grid" style="position:absolute;left:18px;right:18px;top:104px">
      <span>To:</span><span>From:</span><span>Fax:</span><span>Phone:</span><span>Pages:</span><span>Date:</span><span>Re:</span><span>CC:</span>
    </div>
    <div class="checks" style="position:absolute;left:18px;top:188px">
      <span>Urgent</span><span>For Review</span><span>Please Comment</span><span>Please Reply</span><span>Please Recycle</span>
    </div>
    <svg class="swoosh" style="top:268px;height:90px" aria-hidden="true"><use href="#swoosh" width="100%" height="100%"/></svg>
    <div class="footer-contact" style="bottom:10px">
      4629 Larkmoor Rd Ste 310, Albany NY 12203<br>518-926-3081 · 888-547-2263<br>http://TranceGuideNow.example
    </div>
  </section>

  <!-- Envelope back -->
  <section class="piece envelope-back" style="left:782px;top:578px;width:366px;height:120px">
    <svg style="position:absolute;left:0;top:0;width:100%;height:100%" viewBox="0 0 100 40" preserveAspectRatio="none" aria-hidden="true">
      <path d="M0,0 L100,0 L100,6 Q50,32 0,6Z" fill="#7cbc2a"/>
      <path d="M0,0 L100,0 L100,3 Q50,28 0,3Z" fill="#2b3d9c"/>
      <path d="M0,0 L100,0 L100,1 Q50,20 0,1Z" fill="#17215e"/>
      <path d="M0,40 L50,22 L100,40" fill="none" stroke="#ddd" stroke-width=".4"/>
    </svg>
    <div style="position:absolute;left:175px;top:30px;width:14px;height:14px;border-radius:50%;background:var(--green)"></div>
  </section>

  <!-- Envelope front -->
  <section class="piece envelope-front" style="left:740px;top:640px;width:390px;height:143px">
    <div class="brand" style="position:absolute;left:16px;top:14px;font-size:9px">Trance Guide Coaching</div>
    <div class="contact contact--dark" style="position:absolute;left:16px;top:28px;font-size:6px">4629 Larkmoor Rd Ste 310<br>Albany NY 12203</div>
    <div class="faint-mark" role="img" aria-label="Faint brand circle" style="left:280px;top:20px;width:60px;height:60px"></div>
    <svg class="swoosh" style="top:88px;height:55px" aria-hidden="true"><use href="#swoosh" width="100%" height="100%"/></svg>
    <div class="footer-contact" style="bottom:6px">http://TranceGuideNow.example</div>
  </section>

  <!-- Business cards -->
  <section class="card card--blue" style="left:98px;top:822px;width:140px;height:78px">
    <svg class="swoosh" style="top:0;height:30px;transform:scaleY(-1)" aria-hidden="true"><use href="#swoosh-up" width="100%" height="100%"/></svg>
    <div class="contact" style="position:absolute;left:10px;top:34px;font-size:7px;font-weight:700">Gordon P Whitfield</div>
    <div class="contact" style="position:absolute;left:10px;top:45px;font-size:5.5px">Certified Life Coach<br>518-926-3081 · http://TranceGuideNow.example</div>
  </section>
  <section class="card card--blue" style="left:252px;top:822px;width:134px;height:78px">
    <div class="brand brand--light" style="position:absolute;left:12px;top:35px;font-size:7px">Trance Guide Coaching</div>
  </section>
  <section class="card card--white" style="left:410px;top:822px;width:134px;height:78px">
    <div class="brand" style="position:absolute;left:10px;top:14px;font-size:7px">Trance Guide Coaching</div>
    <svg class="swoosh" style="top:44px;height:34px" aria-hidden="true"><use href="#swoosh" width="100%" height="100%"/></svg>
  </section>
  <section class="card card--green" style="left:568px;top:822px;width:124px;height:78px">
    <div class="contact" style="position:absolute;left:10px;bottom:8px;font-size:5.5px">http://TranceGuideNow.example</div>
  </section>

</main>
</body>
</html>
```